Income Tax and Accounting Brochure

I need a brochure using my new logo (file attached). I do tax work and accounting work. I am an EA (QDX Enrolled Agent - logo attached) and would like this incorporated into the brochure. I also have a MSA in Accounting. Please incorporate the text that I have provided in the brochure.

Target Market(s)

Tax Clients - both business and individuals

Industry/Entity Type

Accounting

Colors
0054AA
0677BA
7BADD7
CADEEF
E8F1F8

Requirements
Must have
• Use my logo and the QDX EA file in the brochure
Nice to have
• I would like to see a brochure that I can customize with my own text if possible.

```html
<!DOCTYPE html>
<html lang="en">
<head>
<meta charset="utf-8">
<title>Harlow Ledger &amp; Advisory – Tax Preparation Brochure</title>
<link rel="stylesheet" href="https://fonts.googleapis.com/css2?family=Poppins:wght@400;600;700&display=swap">
<style>
  :root {
    --navy: #0054AA;
    --blue: #0677BA;
    --sky: #7BADD7;
    --mist: #CADEEF;
    --ice: #E8F1F8;
    --ink: #1d1d1f;
    --mat: #cbcbcd;
    --white: #ffffff;
  }
  * { margin: 0; padding: 0; box-sizing: border-box; }
  html, body { width: 1200px; height: 929px; overflow: hidden; background: var(--mat); }
  .stage {
    width: 1292px; height: 1000px; position: relative;
    transform: scale(0.92879); transform-origin: 0 0;
    font-family: "Poppins", sans-serif;
  }
  .brochure { position: absolute; left: 88px; top: 66px; width: 1122px; height: 868px; overflow: hidden; }
  .brochure-bg { position: absolute; inset: 0; }
  .block { position: absolute; }
  .heading { color: var(--blue); font-weight: 700; font-size: 17.5px; line-height: 1.2; }
  .body-copy { color: var(--ink); font-size: 14.6px; line-height: 17px; }
  .body-copy p + p { margin-top: 17px; }
  .on-blue { color: var(--white); font-size: 14.6px; line-height: 17px; }
  .rule { position: absolute; height: 1.5px; width: 54px; }
  .rule-blue { background: var(--blue); }
  .rule-white { background: var(--white); }
  .tick { position: absolute; width: 27px; height: 27px; }
  .business-box {
    position: absolute; left: 712px; top: 649px; width: 410px; height: 156px;
    background: rgba(123, 173, 215, 0.88); border-radius: 22px 0 0 22px;
    padding: 8px 20px 0 75px; color: var(--white); font-size: 14.4px; line-height: 17px;
  }
  .brand { position: absolute; left: 17px; top: 770px; display: flex; align-items: center; gap: 8px; }
  .brand-mark { width: 52px; height: 52px; border-radius: 50%; background: var(--navy); }
  .brand-name { color: var(--navy); font-weight: 600; font-size: 14px; line-height: 17px; letter-spacing: 0.5px; text-transform: uppercase; }
</style>
</head>
<body>
<div class="stage">
  <div class="brochure">
    <svg class="brochure-bg" width="1122" height="868" viewBox="0 0 1122 868" aria-hidden="false">
      <defs>
        <linearGradient id="deskTone" x1="0" y1="0" x2="1" y2="1">
          <stop offset="0" stop-color="#d9cfc4"/>
          <stop offset="0.45" stop-color="#ece8e3"/>
          <stop offset="1" stop-color="#f3f2f1"/>
        </linearGradient>
      </defs>
      <rect width="1122" height="868" fill="var(--white)"/>
      <rect x="374" y="0" width="374" height="868" fill="var(--blue)"/>
      <polygon points="217,639 1122,314 1122,868 340,868" fill="url(#deskTone)" role="img" aria-label="Photo of two people working at a desk with a calculator, pencil and financial charts"/>
    </svg>

    <h2 class="block heading" style="left:37px; top:44px;">Tax Preparation – why hire us?</h2>
    <div class="block body-copy" style="left:37px; top:92px; width:312px;">
      <p>Preparing your own income tax return can be a task that leaves you with more questions than answers. According to a study released by the Federal Audit Bureau last year, most taxpayers (77% of 71 million taxpayers) believe they benefited from using a professional tax preparer.</p>
      <p>Whether we like it or not, today's tax laws are so complicated that filing a relatively simple return can be confusing. It is just too easy to overlook deductions and credits to which you are entitled. Even if you use a computer software program there's no substitute for the assistance of an experienced tax professional.<br>Here's what your get...</p>
    </div>
    <span class="rule rule-blue" style="left:38px; top:421px;"></span>

    <svg class="tick" style="left:410px; top:42px;" viewBox="0 0 27 27"><circle cx="13.5" cy="13.5" r="13.5" fill="var(--sky)"/><path d="M7.5 13.8l4 4 8-8.2" fill="none" stroke="var(--white)" stroke-width="3" stroke-linecap="round" stroke-linejoin="round"/></svg>
    <p class="block on-blue" style="left:411px; top:89px; width:252px;">Your tax return will be checked and rechecked by our computer software identifying potential problems the QDX may look at more closely and reviewing the math to limit QDX contacts.</p>
    <span class="rule rule-white" style="left:411px; top:205px;"></span>

    <svg class="tick" style="left:499px; top:231px;" viewBox="0 0 27 27"><circle cx="13.5" cy="13.5" r="13.5" fill="var(--sky)"/><path d="M7.5 13.8l4 4 8-8.2" fill="none" stroke="var(--white)" stroke-width="3" stroke-linecap="round" stroke-linejoin="round"/></svg>
    <p class="block on-blue" style="left:500px; top:278px; width:230px;">Your tax return can be filed electronically so you will get a refund back quicker.</p>
    <span class="rule rule-white" style="left:500px; top:348px;"></span>

    <svg class="tick" style="left:410px; top:360px;" viewBox="0 0 27 27"><circle cx="13.5" cy="13.5" r="13.5" fill="var(--sky)"/><path d="M7.5 13.8l4 4 8-8.2" fill="none" stroke="var(--white)" stroke-width="3" stroke-linecap="round" stroke-linejoin="round"/></svg>
    <p class="block on-blue" style="left:411px; top:408px; width:250px;">Our staff will show you how to adjust your payroll withholding to get more money back each week. Why give the QDX an interest free loan for up to 16 months.</p>
    <span class="rule rule-white" style="left:411px; top:511px;"></span>

    <svg class="tick" style="left:766px; top:42px;" viewBox="0 0 27 27"><circle cx="13.5" cy="13.5" r="13.5" fill="var(--navy)"/><path d="M7.5 13.8l4 4 8-8.2" fill="none" stroke="var(--white)" stroke-width="3" stroke-linecap="round" stroke-linejoin="round"/></svg>
    <p class="block body-copy" style="left:809px; top:40px; width:245px;">Our staff will show you how to adjust your payroll withholding to get more money back each week. Why give the QDX an interest free loan for up to 16 months.</p>

    <svg class="tick" style="left:766px; top:149px;" viewBox="0 0 27 27"><circle cx="13.5" cy="13.5" r="13.5" fill="var(--navy)"/><path d="M7.5 13.8l4 4 8-8.2" fill="none" stroke="var(--white)" stroke-width="3" stroke-linecap="round" stroke-linejoin="round"/></svg>
    <p class="block body-copy" style="left:809px; top:143px; width:240px;">We will show you potential deductions to limit your tax liability for next year. In addition, we will give you a sheet of commonly overlooked deductions to limit the following year's tax liability.</p>

    <h2 class="block heading" style="left:809px; top:282px;">Books a Mess: No Problem!</h2>

    <div class="business-box">If you own a small business and haven't kept up your bookkeeping, don't worry. We can help you. We'll prepare your bookkeeping for the year, prepare a full Schedule C, as well as your personal income tax return. Then we'll help you set up an easy system that allows you to keep your books in tip-top shape next year.</div>

    <div class="brand">
      <span class="brand-mark"></span>
      <span class="brand-name">Harlow Ledger<br>&amp; Advisory, LLC</span>
    </div>
  </div>
</div>
</body>
</html>
```